Career Drop Down Layout on CopperTrailhead.com Quiz Results

We want to redesign the career drop down view after people take the career finder quiz at CopperTrailhead.com. After you take the quiz (feel free to take it yourself), you get a results page. On the left hand navigation bar, go to Career Matches (in green). When you open one of your career matches, we want people to see lots of great information about the job. We need help figuring out how to display the information. The information we want to display is the following:

1) name of job
2) WERQ description
3) Link to the Werq info
4) Match dial
5) Bright outlook image
6) a video about the job
7) Average salary
8) Minimum Qualifications
9) Top Tips
10) Recommended Programs
11) Jobs in their area - by Hireloop Finder

I put screen shots of what we have now and a mock-up of the new elements in the brief. It can look anyway you think will be good. I'm not tied to the mock-up at all.

To see how your design will look live on the web do the following:

1) Login at: https://www.coppertrailhead.com/survey/login (or take the quiz yourself to see your own results)
2) Enter Email address: marla.voss@copperventure.org
3) Enter Password: 123456
4) See results summary - Click on Career Matches from the left navigation bar
5) See the career matches, when you click the arrow on the right side of each career match it will display the new page you are designing for each career with info from a database.

Thanks, Marla

Target Market(s)

Young people looking for jobs

Number of Pages Required

1 page

Requirements
Must have
• The layout of how all the information will look nicely on a computer screen. It can scroll down more vertically if necessary.

The color scheme and text must match the existing site since this page will be embedded in our site. I attached our design guide.
Nice to have
• I'd like to see a very easy to scan, organized way to display a lot of job information.

```html
<!DOCTYPE html>
<html lang="en">
<head>
<meta charset="utf-8">
<title>Career Matches – Copper Trailhead</title>
<link href="https://fonts.googleapis.com/css2?family=Lato:wght@400;700&display=swap" rel="stylesheet">
<style>
:root{
  --purple:#4f3f9a;
  --purple-dark:#3f3185;
  --green:#76c043;
  --green-dark:#3d7a3a;
  --ink:#222;
  --muted:#555;
  --line:#bbb;
  --orange:#f39a1e;
  --link:#2c2a8c;
}
*{box-sizing:border-box;margin:0;padding:0}
html,body{width:799px;height:1200px;overflow:hidden;background:#fff;font-family:'Lato',sans-serif;color:var(--ink)}
.page{position:relative;width:799px;height:1200px}
.abs{position:absolute}

.topbar{left:0;top:0;width:799px;height:39px;border-bottom:1px solid #ddd;background:#fff}
.brand{left:15px;top:15px;font-size:11px;font-weight:700;color:var(--green)}
.brand span{color:var(--purple)}
.topnav{right:24px;top:8px;display:flex;align-items:center;gap:15px;font-size:6.5px;color:#333}
.logout{background:var(--purple);color:#fff;border-radius:12px;padding:8px 12px;font-weight:700}

.sidebar{left:0;top:39px;width:168px;height:1062px;background:var(--purple)}
.sidebar h2{color:#fff;font-size:12px;text-align:center;margin:22px 0 21px}
.sidenav{list-style:none;border-top:1px solid #8478c2}
.sidenav li{height:18px;line-height:17px;text-align:center;color:#fff;font-size:7.5px;border-bottom:1px solid #8478c2}
.sidenav li.active{background:var(--green-dark);font-weight:700}
.pdf{display:block;margin:6px auto 0;width:92px;height:17px;border-radius:9px;background:var(--green);color:#fff;font-size:8.5px;text-align:center;line-height:17px;box-shadow:0 1px 2px rgba(0,0,0,.3)}

.title{left:168px;width:631px;top:62px;text-align:center}
.title h1{display:inline-flex;align-items:center;gap:5px;font-size:18.5px;font-weight:700}
.title .dot{width:32px;height:32px;border-radius:50%;background:var(--green)}
.lead{left:168px;width:631px;top:108px;text-align:center;font-size:8.5px;line-height:14px}
.mini{display:inline-block;width:10px;height:10px;border-radius:50%;vertical-align:-2px;border:1px solid #333}

.sechead{left:204px;width:560px;display:flex;align-items:center;gap:6px}
.sechead .ic{width:27px;height:27px;border-radius:50%;background:var(--green)}
.sechead h3{font-size:15px;font-weight:400;color:#444}
.sechead .rule{flex:1;height:1px;background:#999;margin-left:4px}
.divider{left:204px;width:560px;height:1px;background:#999}

.card{width:184px;height:284px;border:1px solid var(--line);background:#fff}
.jobbar{height:41px;background:var(--green);display:flex;align-items:center;padding-left:7px;gap:4px;color:#fff;font-size:10px}
.rate{width:15px;height:15px;border-radius:50%;border:1px solid #2e5a1e}
.rate.up{background:#fff}.rate.mid{background:#9fd47a}.rate.down{background:#d9914a}
.jobbar b{font-weight:400;margin-left:3px;font-size:10.5px}
.jobbody{padding:0 8px}
.jobbody h4{font-size:10px;font-weight:400;color:#444;margin:20px 0 12px}
.jobbody h5{font-size:10px;font-weight:400;color:#333;margin-bottom:4px}
.jobbody p{font-size:6.5px;line-height:11px;color:var(--muted)}
.werq{display:block;width:156px;height:18px;margin-top:16px;border-radius:9px;background:var(--green);color:#fff;font-size:7px;font-weight:700;text-align:center;line-height:18px}

.center{text-align:center}
.gauge{display:block;margin:14px auto 0}
.match{font-size:10px;color:#333;margin-top:4px}
.outlook{font-size:18px;font-weight:700;color:var(--orange);margin-top:10px}
.video{display:block;margin:8px auto 0;width:136px;height:93px;background:linear-gradient(90deg,#6b6b6b 0 50%,#4a3a8c 50%)}
.facts{font-size:10px;color:#333;line-height:18px;margin-top:8px}

.tips{padding:20px 10px 0}
.tips h4{font-size:10px;font-weight:400;color:#444;margin-bottom:7px}
.tips p{font-size:6.5px;line-height:11px;color:var(--muted)}
.tips .more{font-size:6.5px;color:#222;text-decoration:underline;display:block;margin:12px 0 15px}
.tips h5{font-size:10px;font-weight:400;color:#444;margin-bottom:5px}
.tips .prog{font-size:7.5px;color:var(--link);text-decoration:underline;line-height:15px;display:block}
.tips .jobs{font-size:9px;color:var(--link);margin-top:9px}
.finder{display:flex;align-items:center;gap:4px;font-size:11px;font-weight:700;color:#333;margin-top:8px}
.finder i{width:9px;height:9px;background:var(--green)}

.pager{left:395px;top:897px;height:28px;display:flex;box-shadow:0 0 3px rgba(0,0,0,.2);font-size:15px;color:#666}
.pager span{width:26px;text-align:center;line-height:28px;border-right:1px solid #ddd}
.pager .on{background:var(--green);color:#2d5f1e}

.pill{top:977px;height:18px;border-radius:9px;color:#fff;font-size:10.5px;font-weight:700;display:flex;align-items:center;gap:5px;padding:0 7px 0 2px;box-shadow:0 1px 2px rgba(0,0,0,.3)}
.pill i{width:15px;height:15px;border-radius:50%;background:#fff}
.why{left:338px;background:#a43fb0}
.what{left:488px;background:#2d5e7e}

.step{top:1037px;font-size:12.5px;color:#222;display:flex;align-items:center;gap:5px}
.step i{width:12px;height:12px;border-radius:50%;background:#a89ee0}

.footer{left:0;top:1101px;width:799px;height:77px;border-top:1px solid #ddd;background:#fff}
.social{left:236px;top:1115px;display:flex;gap:46px}
.social i{width:17px;height:17px;border-radius:50%;background:#111;display:block}
.social svg{display:block}
.links{left:217px;top:1150px;display:flex;gap:20px;font-size:11.5px;color:#111}
.copy{left:0;top:1178px;width:799px;height:22px;background:#000;color:#fff;font-size:10px;text-align:center;line-height:22px}
</style>
</head>
<body>
<div class="page">

<header class="topbar abs">
  <div class="brand abs">Copper <span>Trailhead</span></div>
  <nav class="topnav abs"><span>HOME</span><span>MY RESULTS ▾</span><span>SERVICES ▾</span><span class="logout">LOG OUT</span></nav>
</header>

<aside class="sidebar abs">
  <h2>Marla's Results</h2>
  <ul class="sidenav">
    <li>Results Summary</li><li>What Motivates You</li><li>Your DISC Profile</li>
    <li class="active">Career Matches</li><li>Maximize My Results</li><li>Communication Tips</li>
    <li>Reflections and Goals</li><li>Resources</li>
  </ul>
  <span class="pdf">Download PDF</span>
</aside>

<div class="title abs"><h1><span class="dot"></span>Career Matches</h1></div>
<p class="lead abs">Rate as many jobs as you can, <span class="mini" style="background:#9fd47a"></span> = send to favorites, <span class="mini" style="background:#ccc"></span> = Not sure, <span class="mini" style="background:#e03a3a"></span> = No way - send to archive!<br>Click on each category for in-depth descriptions, resources, education options, and tips.</p>

<!-- Match one -->
<div class="sechead abs" style="top:168px"><span class="ic"></span><h3>Favorites</h3><span class="rule"></span></div>

<section class="card abs" style="left:204px;top:203px">
  <div class="jobbar"><span class="rate up"></span><span class="rate mid"></span><span class="rate down"></span><b>Social Entrepreneurism</b></div>
  <div class="jobbody">
    <h4>Industry: Entrepreneurism</h4>
    <h5>WERQ job description:</h5>
    <p>Determine and formulate policies and provide overall direction of companies or private and public sector organizations within guidelines set up by a board of directors or similar governing body. Plan, direct, or coordinate operational activities at the highest level of management with the help of subordinate executives and staff managers.</p>
    <span class="werq">Learn More About this Job on WERQ</span>
  </div>
</section>

<section class="card abs center" style="left:392px;top:203px">
  <svg class="gauge" width="128" height="68" viewBox="0 0 128 68" aria-label="Match dial">
    <path d="M4 64 A60 60 0 0 1 124 64" fill="none" stroke="#999" stroke-width="12"/>
    <path d="M22 64 A42 42 0 0 1 27 44 L64 64Z" fill="#d7282a"/>
    <path d="M27 44 A42 42 0 0 1 45 27 L64 64Z" fill="#f26d22"/>
    <path d="M45 27 A42 42 0 0 1 80 25 L64 64Z" fill="#f0c929"/>
    <path d="M80 25 A42 42 0 0 1 100 42 L64 64Z" fill="#8cc63f"/>
    <path d="M100 42 A42 42 0 0 1 106 64 L64 64Z" fill="#4f3f9a"/>
    <line x1="64" y1="64" x2="90" y2="30" stroke="#111" stroke-width="3"/>
    <circle cx="64" cy="64" r="6" fill="#111"/>
    <text x="64" y="9" font-size="5.5" text-anchor="middle" font-weight="700" fill="#222">GOOD</text>
  </svg>
  <div class="match">Your match level (11)</div>
  <div class="outlook">Bright Outlook</div>
  <div class="video" role="img" aria-label="Video about the job: Trailhead Talks on entrepreneurs"></div>
  <div class="facts">Average Nationwide Salary: $35,950<br>Minimum Qualifications: None</div>
</section>

<section class="card abs" style="left:580px;top:203px">
  <div class="tips">
    <h4>Top Tips</h4>
    <p>What is an Entrepreneur?<br>An entrepreneur is someone who starts their own business and looks for opportunity. Maybe you want to run the next big tech company. Maybe you want to act as an independent consultant for other businesses or sell your products at a farmer's...</p>
    <span class="more">Read More</span>
    <h5>Recommended Programs:</h5>
    <span class="prog">Brightmark Fellows, US office located in Arlington</span>
    <span class="prog">Fieldstone Accelerator</span>
    <span class="prog">Common Good Network</span>
    <div class="jobs" style="text-decoration:underline">Jobs in their area - by</div>
    <div class="finder"><i></i>Hireloop Finder</div>
  </div>
</section>

<div class="divider abs" style="top:509px"></div>

<!-- Match two -->
<div class="sechead abs" style="top:520px"><span class="ic"></span><h3>Favorites</h3><span class="rule"></span></div>

<section class="card abs" style="left:204px;top:555px">
  <div class="jobbar"><span class="rate up"></span><span class="rate mid"></span><span class="rate down"></span><b>Life Coaching</b></div>
  <div class="jobbody">
    <h4>Industry: Life Coaching</h4>
    <h5>WERQ job description:</h5>
    <p>Counsel individuals to maximize the independence and employability of persons coping with personal, social, and vocational difficulties that result from birth defects, illness, disease, accidents, aging, or the stress of daily life. Coordinate activities for residents of care and treatment facilities. Assess client needs and design and implement rehabilitation programs that may include personal and vocational counseling, training, and job placement.</p>
    <span class="werq">Learn More About this Job on WERQ</span>
  </div>
</section>

<section class="card abs center" style="left:392px;top:555px">
  <svg class="gauge" width="128" height="68" viewBox="0 0 128 68" aria-label="Match dial">
    <path d="M4 64 A60 60 0 0 1 124 64" fill="none" stroke="#999" stroke-width="12"/>
    <path d="M22 64 A42 42 0 0 1 27 44 L64 64Z" fill="#d7282a"/>
    <path d="M27 44 A42 42 0 0 1 45 27 L64 64Z" fill="#f26d22"/>
    <path d="M45 27 A42 42 0 0 1 80 25 L64 64Z" fill="#f0c929"/>
    <path d="M80 25 A42 42 0 0 1 100 42 L64 64Z" fill="#8cc63f"/>
    <path d="M100 42 A42 42 0 0 1 106 64 L64 64Z" fill="#4f3f9a"/>
    <line x1="64" y1="64" x2="90" y2="30" stroke="#111" stroke-width="3"/>
    <circle cx="64" cy="64" r="6" fill="#111"/>
    <text x="64" y="9" font-size="5.5" text-anchor="middle" font-weight="700" fill="#222">GOOD</text>
  </svg>
  <div class="match">Your match level (12)</div>
  <div class="outlook">Bright Outlook</div>
  <div class="video" role="img" aria-label="Video about the job: Trailhead Talks on entrepreneurs"></div>
  <div class="facts">Average Nationwide Salary: $64,380<br>Minimum Qualifications: None</div>
</section>

<section class="card abs" style="left:580px;top:555px">
  <div class="tips">
    <h4>Top Tips</h4>
    <p>What is an Entrepreneur?<br>An entrepreneur is someone who starts their own business and looks for opportunity. Maybe you want to run the next big tech company. Maybe you want to act as an independent consultant for other businesses or sell your products at a farmer's...</p>
    <span class="more">Read More</span>
    <h5>Recommended Programs:</h5>
    <span class="prog">Brightmark Fellows, US office located in Arlington</span>
    <span class="prog">Fieldstone Accelerator</span>
    <span class="prog">Common Good Network</span>
    <div class="jobs" style="color:#222">Jobs in their area - by</div>
    <div class="finder"><i></i>Hireloop Finder</div>
  </div>
</section>

<div class="divider abs" style="top:862px"></div>

<nav class="pager abs"><span>&lt;</span><span class="on">1</span><span>2</span><span>3</span><span>4</span><span>5</span><span style="border:0">&gt;</span></nav>

<div class="pill why abs"><i></i>Why is this important?</div>
<div class="pill what abs"><i></i>What can I do with this?</div>

<div class="step abs" style="left:265px"><i></i>Your DISC Profile</div>
<div class="step abs" style="left:572px">Maximize My Results<i></i></div>

<footer class="footer abs"></footer>
<div class="social abs" aria-label="Social links">
  <i></i><i></i><i></i><i></i><i></i>
  <svg width="17" height="17" viewBox="0 0 17 17" aria-label="Email"><rect x="1.5" y="4" width="14" height="9" fill="none" stroke="#111"/><path d="M1.5 4 L8.5 9.5 L15.5 4" fill="none" stroke="#111"/></svg>
</div>
<nav class="links abs"><span>NEWS</span><span>PRIVACY POLICY</span><span>TERMS &amp; CONDITIONS</span><span>CONTACT US</span></nav>
<div class="copy abs">Copyright Copper Trail Education Company © 2021</div>

</div>
</body>
</html>
```